Birthday Calendar: Dec 1 - Nov 30

This calendar should have three parts. First the center should contain an annual calendar beginning December 1, 2019 and going through November 30, 2020. I'm picturing the months and date numbers - no need for individual boxes for each day. Second, above the calendar should be blank space (intended for people to write words of advise and love). Third, beneath the calendar space will be several statements about the year (i.e. "If you have client meetings four times a month, you'll meet with 36 clients." "If you kiss your kids only once each day, that's 1,460 kisses.") I don't have an exact overall size of the calendar in mind, but definitely know it will need to be bigger than 8.5"x11"

Target Market(s)

Wife - Her birthday is November 30, so this is a calendar to mark the time from one birthday to the next.

Font styles to use
Serif

Colors

Designer to choose colors to be used in the design.

Requirements
Must have
• The three different sections listed in the description. There will be 12 people handwriting simple phrases of advise (for how to have the best year) at the top, so there should be enough room for that. At the top it should say "These are the Days"
• I will provide the complete set of statements that will appear at the bottom of the calendar. There will be 10 (or less) statements total, sort of like the ones provided in the description. Let me know when you want those statements.

```html
<!DOCTYPE html>
<html lang="en">
<head>
<meta charset="utf-8">
<title>These are the Days – Birthday Calendar</title>
<link href="https://fonts.googleapis.com/css2?family=Courgette&family=Montserrat:ital,wght@0,400;0,600;0,700;1,600;1,700&family=Lato:wght@300&family=Playfair+Display:wght@900&family=Lora:ital@1&display=swap" rel="stylesheet">
<style>
  :root {
    --backdrop: #2b4a9e;
    --paper: #dcedf0;
    --note-box: #eef4f5;
    --card: #f4f6f7;
    --ink: #1c1c1e;
    --band: #2f2d6c;
    --cream: #f3efe4;
    --sky: #3aa8dc;
    --sun: #f3e84a;
    --magenta: #e5288f;
    --orange: #f29a2c;
    --red: #e3302f;
    --lime: #8cc63f;
  }
  * { box-sizing: border-box; margin: 0; padding: 0; }
  html, body { width: 1180px; height: 1200px; overflow: hidden; }
  body { background: var(--backdrop); position: relative; font-family: "Montserrat", sans-serif; }

  .poster {
    position: absolute; left: 230px; top: 37px;
    width: 720px; height: 1125px;
    background: var(--paper);
    overflow: hidden;
  }

  .poster-title {
    position: absolute; left: 0; top: 8px; width: 720px;
    font-family: "Courgette", cursive; font-weight: 400; font-size: 22px;
    line-height: 30px; text-align: center; color: var(--ink);
  }

  /* advice notes */
  .notes {
    position: absolute; left: 33px; top: 44px;
    display: grid; grid-template-columns: repeat(3, 215px);
    grid-template-rows: repeat(4, 44px);
    column-gap: 5px; row-gap: 5px;
  }
  .note { background: var(--note-box); border-radius: 6px; }

  /* months */
  .month { position: absolute; width: 206px; }
  .month-title {
    font-family: "Courgette", cursive; font-weight: 400; font-size: 19px; color: var(--ink);
    text-align: center; height: 28px; line-height: 24px;
  }
  .month-card { background: var(--card); border-radius: 8px; height: 133px; overflow: hidden; }
  .weekdays {
    background: var(--ink); color: #fff; border-radius: 8px;
    height: 16px; display: grid; grid-template-columns: repeat(7, 28px);
    padding-left: 7px; font-size: 7.5px; font-weight: 600; line-height: 16px; text-align: center;
  }
  .days {
    display: grid; grid-template-columns: repeat(7, 28px); grid-auto-rows: 18.5px;
    padding: 3px 0 0 7px; font-size: 8.5px; font-weight: 700; font-style: italic;
    text-align: center; line-height: 18.5px; color: var(--ink);
  }
  .start-2 span:first-child { grid-column-start: 2; }
  .start-3 span:first-child { grid-column-start: 3; }
  .start-4 span:first-child { grid-column-start: 4; }
  .start-5 span:first-child { grid-column-start: 5; }
  .start-6 span:first-child { grid-column-start: 6; }
  .start-7 span:first-child { grid-column-start: 7; }

  .c1 { left: 30px; } .c2 { left: 256px; } .c3 { left: 480px; }
  .r1 { top: 262px; } .r2 { top: 430px; } .r3 { top: 598px; } .r4 { top: 766px; }

  /* statements band */
  .stats {
    position: absolute; left: 0; top: 945px; width: 720px; height: 180px;
    background: var(--band); color: var(--cream);
  }
  .stat-num { position: absolute; line-height: 1; white-space: nowrap; }
  .thin { font-family: "Lato", sans-serif; font-weight: 300; }
  .bold { font-family: "Playfair Display", serif; font-weight: 900; }
  .stat-text { position: absolute; font-size: 8px; line-height: 1.25; }
  .serif-note { font-family: "Lora", serif; font-style: italic; }
  .sans-note { font-family: "Montserrat", sans-serif; }
  .center { text-align: center; }
</style>
</head>
<body>
<main class="poster">

  <h1 class="poster-title">These are the Days</h1>

  <section class="notes" aria-label="Space for handwritten advice">
    <div class="note"></div><div class="note"></div><div class="note"></div>
    <div class="note"></div><div class="note"></div><div class="note"></div>
    <div class="note"></div><div class="note"></div><div class="note"></div>
    <div class="note"></div><div class="note"></div><div class="note"></div>
  </section>

  <section class="calendar" aria-label="December 2019 to November 2020">
    <div class="month c1 r1"><h2 class="month-title">December 2019</h2><div class="month-card"><div class="weekdays"><span>SUN</span><span>MON</span><span>TUE</span><span>WED</span><span>THU</span><span>FRI</span><span>SAT</span></div><div class="days start-1"><span>1</span><span>2</span><span>3</span><span>4</span><span>5</span><span>6</span><span>7</span><span>8</span><span>9</span><span>10</span><span>11</span><span>12</span><span>13</span><span>14</span><span>15</span><span>16</span><span>17</span><span>18</span><span>19</span><span>20</span><span>21</span><span>22</span><span>23</span><span>24</span><span>25</span><span>26</span><span>27</span><span>28</span><span>29</span><span>30</span><span>31</span></div></div></div>
    <div class="month c2 r1"><h2 class="month-title">January 2020</h2><div class="month-card"><div class="weekdays"><span>SUN</span><span>MON</span><span>TUE</span><span>WED</span><span>THU</span><span>FRI</span><span>SAT</span></div><div class="days start-4"><span>1</span><span>2</span><span>3</span><span>4</span><span>5</span><span>6</span><span>7</span><span>8</span><span>9</span><span>10</span><span>11</span><span>12</span><span>13</span><span>14</span><span>15</span><span>16</span><span>17</span><span>18</span><span>19</span><span>20</span><span>21</span><span>22</span><span>23</span><span>24</span><span>25</span><span>26</span><span>27</span><span>28</span><span>29</span><span>30</span><span>31</span></div></div></div>
    <div class="month c3 r1"><h2 class="month-title">February 2020</h2><div class="month-card"><div class="weekdays"><span>SUN</span><span>MON</span><span>TUE</span><span>WED</span><span>THU</span><span>FRI</span><span>SAT</span></div><div class="days start-7"><span>1</span><span>2</span><span>3</span><span>4</span><span>5</span><span>6</span><span>7</span><span>8</span><span>9</span><span>10</span><span>11</span><span>12</span><span>13</span><span>14</span><span>15</span><span>16</span><span>17</span><span>18</span><span>19</span><span>20</span><span>21</span><span>22</span><span>23</span><span>24</span><span>25</span><span>26</span><span>27</span><span>28</span><span>29</span></div></div></div>

    <div class="month c1 r2"><h2 class="month-title">March 2020</h2><div class="month-card"><div class="weekdays"><span>SUN</span><span>MON</span><span>TUE</span><span>WED</span><span>THU</span><span>FRI</span><span>SAT</span></div><div class="days start-1"><span>1</span><span>2</span><span>3</span><span>4</span><span>5</span><span>6</span><span>7</span><span>8</span><span>9</span><span>10</span><span>11</span><span>12</span><span>13</span><span>14</span><span>15</span><span>16</span><span>17</span><span>18</span><span>19</span><span>20</span><span>21</span><span>22</span><span>23</span><span>24</span><span>25</span><span>26</span><span>27</span><span>28</span><span>29</span><span>30</span><span>31</span></div></div></div>
    <div class="month c2 r2"><h2 class="month-title">April 2020</h2><div class="month-card"><div class="weekdays"><span>SUN</span><span>MON</span><span>TUE</span><span>WED</span><span>THU</span><span>FRI</span><span>SAT</span></div><div class="days start-4"><span>1</span><span>2</span><span>3</span><span>4</span><span>5</span><span>6</span><span>7</span><span>8</span><span>9</span><span>10</span><span>11</span><span>12</span><span>13</span><span>14</span><span>15</span><span>16</span><span>17</span><span>18</span><span>19</span><span>20</span><span>21</span><span>22</span><span>23</span><span>24</span><span>25</span><span>26</span><span>27</span><span>28</span><span>29</span><span>30</span></div></div></div>
    <div class="month c3 r2"><h2 class="month-title">May 2020</h2><div class="month-card"><div class="weekdays"><span>SUN</span><span>MON</span><span>TUE</span><span>WED</span><span>THU</span><span>FRI</span><span>SAT</span></div><div class="days start-6"><span>1</span><span>2</span><span>3</span><span>4</span><span>5</span><span>6</span><span>7</span><span>8</span><span>9</span><span>10</span><span>11</span><span>12</span><span>13</span><span>14</span><span>15</span><span>16</span><span>17</span><span>18</span><span>19</span><span>20</span><span>21</span><span>22</span><span>23</span><span>24</span><span>25</span><span>26</span><span>27</span><span>28</span><span>29</span><span>30</span><span>31</span></div></div></div>

    <div class="month c1 r3"><h2 class="month-title">June 2020</h2><div class="month-card"><div class="weekdays"><span>SUN</span><span>MON</span><span>TUE</span><span>WED</span><span>THU</span><span>FRI</span><span>SAT</span></div><div class="days start-2"><span>1</span><span>2</span><span>3</span><span>4</span><span>5</span><span>6</span><span>7</span><span>8</span><span>9</span><span>10</span><span>11</span><span>12</span><span>13</span><span>14</span><span>15</span><span>16</span><span>17</span><span>18</span><span>19</span><span>20</span><span>21</span><span>22</span><span>23</span><span>24</span><span>25</span><span>26</span><span>27</span><span>28</span><span>29</span><span>30</span></div></div></div>
    <div class="month c2 r3"><h2 class="month-title">July 2020</h2><div class="month-card"><div class="weekdays"><span>SUN</span><span>MON</span><span>TUE</span><span>WED</span><span>THU</span><span>FRI</span><span>SAT</span></div><div class="days start-4"><span>1</span><span>2</span><span>3</span><span>4</span><span>5</span><span>6</span><span>7</span><span>8</span><span>9</span><span>10</span><span>11</span><span>12</span><span>13</span><span>14</span><span>15</span><span>16</span><span>17</span><span>18</span><span>19</span><span>20</span><span>21</span><span>22</span><span>23</span><span>24</span><span>25</span><span>26</span><span>27</span><span>28</span><span>29</span><span>30</span><span>31</span></div></div></div>
    <div class="month c3 r3"><h2 class="month-title">August 2020</h2><div class="month-card"><div class="weekdays"><span>SUN</span><span>MON</span><span>TUE</span><span>WED</span><span>THU</span><span>FRI</span><span>SAT</span></div><div class="days start-7"><span>1</span><span>2</span><span>3</span><span>4</span><span>5</span><span>6</span><span>7</span><span>8</span><span>9</span><span>10</span><span>11</span><span>12</span><span>13</span><span>14</span><span>15</span><span>16</span><span>17</span><span>18</span><span>19</span><span>20</span><span>21</span><span>22</span><span>23</span><span>24</span><span>25</span><span>26</span><span>27</span><span>28</span><span>29</span><span>30</span><span>31</span></div></div></div>

    <div class="month c1 r4"><h2 class="month-title">September 2020</h2><div class="month-card"><div class="weekdays"><span>SUN</span><span>MON</span><span>TUE</span><span>WED</span><span>THU</span><span>FRI</span><span>SAT</span></div><div class="days start-3"><span>1</span><span>2</span><span>3</span><span>4</span><span>5</span><span>6</span><span>7</span><span>8</span><span>9</span><span>10</span><span>11</span><span>12</span><span>13</span><span>14</span><span>15</span><span>16</span><span>17</span><span>18</span><span>19</span><span>20</span><span>21</span><span>22</span><span>23</span><span>24</span><span>25</span><span>26</span><span>27</span><span>28</span><span>29</span><span>30</span></div></div></div>
    <div class="month c2 r4"><h2 class="month-title">October 2020</h2><div class="month-card"><div class="weekdays"><span>SUN</span><span>MON</span><span>TUE</span><span>WED</span><span>THU</span><span>FRI</span><span>SAT</span></div><div class="days start-5"><span>1</span><span>2</span><span>3</span><span>4</span><span>5</span><span>6</span><span>7</span><span>8</span><span>9</span><span>10</span><span>11</span><span>12</span><span>13</span><span>14</span><span>15</span><span>16</span><span>17</span><span>18</span><span>19</span><span>20</span><span>21</span><span>22</span><span>23</span><span>24</span><span>25</span><span>26</span><span>27</span><span>28</span><span>29</span><span>30</span><span>31</span></div></div></div>
    <div class="month c3 r4"><h2 class="month-title">November 2020</h2><div class="month-card"><div class="weekdays"><span>SUN</span><span>MON</span><span>TUE</span><span>WED</span><span>THU</span><span>FRI</span><span>SAT</span></div><div class="days start-1"><span>1</span><span>2</span><span>3</span><span>4</span><span>5</span><span>6</span><span>7</span><span>8</span><span>9</span><span>10</span><span>11</span><span>12</span><span>13</span><span>14</span><span>15</span><span>16</span><span>17</span><span>18</span><span>19</span><span>20</span><span>21</span><span>22</span><span>23</span><span>24</span><span>25</span><span>26</span><span>27</span><span>28</span><span>29</span><span>30</span></div></div></div>
  </section>

  <section class="stats" aria-label="The year in numbers">
    <div class="stat-num thin" style="left:33px; top:22px; font-size:52px; color:var(--sky);">12</div>
    <p class="stat-text serif-note" style="left:105px; top:28px; width:72px;">The number of events you'll run if you coordinate one each month.</p>

    <div class="stat-num bold" style="left:32px; top:86px; font-size:52px; color:var(--sun);">1460</div>
    <p class="stat-text serif-note center" style="left:30px; top:142px; width:140px;">the number of kisses given if you kiss each kid just once a day.</p>

    <div class="stat-num bold" style="left:201px; top:14px; font-size:76px; color:var(--magenta);">4</div>
    <p class="stat-text sans-note" style="left:199px; top:100px; width:72px;">The number of days devoted entirely to you, if you take two hours a week just for yourself.</p>

    <div class="stat-num bold" style="left:296px; top:20px; font-size:44px; color:var(--sun);">52</div>
    <p class="stat-text sans-note" style="left:360px; top:26px; width:78px; font-size:7.5px;">The people you've made time for if you meet with just one friend each week</p>

    <div class="stat-num thin" style="left:307px; top:77px; font-size:50px; color:var(--sky);">260</div>
    <p class="stat-text serif-note center" style="left:292px; top:132px; width:112px;">The number of family meals shared together if you have just 5 dinners a week.</p>

    <div class="stat-num thin" style="left:459px; top:18px; font-size:50px; color:var(--orange);">156</div>
    <p class="stat-text serif-note center" style="left:452px; top:70px; width:112px;">The number of workouts you can squeeze in if you just do it three times a week.</p>

    <div class="stat-num bold" style="left:428px; top:108px; font-size:48px; color:var(--red);">24</div>
    <p class="stat-text serif-note" style="left:502px; top:112px; width:70px; font-size:7.5px;">The number of cups of coffee shared together if you have just 5 dinners a week.</p>

    <div class="stat-num bold" style="left:590px; top:14px; font-size:64px; color:var(--lime);">20</div>
    <p class="stat-text sans-note" style="left:594px; top:96px; width:104px; font-size:10px; font-weight:700; font-style:italic; color:#fff;">about the number of dates you could go on with Casey if you got out every few weeks</p>
  </section>

</main>
</body>
</html>
```